We are a small business - Tree Care Company owned bt a certified Arborist. We would like an advertis

Hurricane season is approaching. We would like our current and potential customers to hire us for their tree work - safety first.

A little bit about us:

We are GWF-certified and insured, you can be confident that you will be able to trust us on your property. We maintain a clean, organized, and safe working environment.

Our tree service services St Petersburg, Clearwater, Belleair, Seminole, and surrounding tampa bay areas cover anything and everything that you may find yourself needing regarding tree care services.

Some of our specialties include tree pruning and trimming, removal, support, planting, emergency tree service, and much, much more.

For hurricane prep, make sure your trees are properly maintained and inspected for structual issues.

Target Market(s)

late 20's to 65. Homeow

Requirements
Must have
• A Call to action. Call us to schedule a FREE estimate.
• 1-866-413-BOUGH

```html
<!DOCTYPE html>
<html lang="en">
<head>
<meta charset="utf-8">
<title>Canopy Crest Professional Tree Care</title>
<link href="https://fonts.googleapis.com/css2?family=Arimo:wght@400;700&family=Oswald:wght@500;600&display=swap" rel="stylesheet">
<style>
  :root{
    --leaf:#6fbe44;
    --leaf-deep:#2f7d32;
    --forest:#3d8a3a;
    --ink:#2b2b2b;
    --grey:#5a5a5a;
    --panel-grey:#ececec;
    --paper:#ffffff;
    --white:#ffffff;
  }
  *{margin:0;padding:0;box-sizing:border-box}
  html,body{width:931px;height:1200px;overflow:hidden;background:var(--paper)}
  body{font-family:"Arimo",Arial,sans-serif;color:var(--ink)}
  .flyer{position:relative;width:931px;height:1200px;background:var(--paper)}
  .brand{position:absolute;left:0;right:0;top:40px;text-align:center}
  .brand-name{display:flex;align-items:center;justify-content:center;gap:14px;font-size:62px;line-height:1;color:var(--leaf-deep);font-weight:400;letter-spacing:-1px}
  .brand-dot{width:22px;height:22px;border-radius:50%;background:var(--leaf)}
  .brand-rule{width:430px;height:2px;background:var(--grey);margin:18px auto 10px}
  .brand-tag{font-size:19px;letter-spacing:6px;color:var(--grey)}
  .photo{position:absolute}
  .photo-crew{left:35px;top:174px;width:419px;height:473px;background:linear-gradient(180deg,#9cc3e6 0%,#c9dcea 35%,#5f7f45 60%,#4a6a32 100%)}
  .photo-trucks{left:462px;top:349px;width:433px;height:298px;background:linear-gradient(180deg,#4f8fd8 0%,#9fc3e8 40%,#6d8d52 68%,#7b7e80 100%)}
  .photo-loader{left:33px;top:806px;width:421px;height:287px;background:linear-gradient(135deg,#4d6a3a 0%,#7c8a46 40%,#c9a624 70%,#3c3c30 100%)}
  .box{position:absolute;color:var(--white)}
  .about{left:462px;top:174px;width:433px;height:165px;background:var(--leaf);padding:14px 12px}
  .box h2{font-family:"Oswald",sans-serif;font-weight:600;line-height:1}
  .about h2{font-size:34px;margin-bottom:10px}
  .box p{font-size:14.5px;line-height:1.2}
  .areas{left:33px;top:658px;width:421px;height:139px;background:var(--leaf-deep);padding:20px 10px}
  .areas h2{font-size:45px;letter-spacing:1px;margin-bottom:10px}
  .specs-head{position:absolute;left:462px;top:658px;width:433px;height:82px;background:var(--panel-grey);display:flex;align-items:center;justify-content:center}
  .specs-head h2{font-family:"Oswald",sans-serif;font-weight:600;font-size:48px;color:var(--leaf-deep);letter-spacing:1px}
  .specs{position:absolute;left:462px;top:740px;width:433px;height:353px;background:linear-gradient(135deg,#5aa83a 0%,#3f9130 50%,#2f7a28 100%)}
  .specs ul{list-style:none;padding:12px 0 0 28px}
  .specs li{display:flex;align-items:center;gap:18px;height:46px;color:var(--white);font-size:18px}
  .specs li:last-child{height:60px;line-height:1.15}
  .specs svg{flex:none}
  .footer{position:absolute;left:0;top:1103px;width:931px;height:97px;display:flex}
  .footer-cta{width:474px;background:var(--ink);color:var(--white);padding:12px 0 0 34px}
  .cta-line{font-size:23px;display:inline-block;border-bottom:1.5px solid var(--white);padding-bottom:3px}
  .cta-line strong{color:var(--leaf);font-weight:700}
  .contact{display:flex;align-items:center;margin-top:8px}
  .phone{font-family:"Oswald",sans-serif;font-weight:500;font-size:25px;letter-spacing:.5px;padding-right:12px;border-right:1.5px solid var(--white)}
  .web{display:flex;align-items:center;gap:5px;padding-left:10px;font-size:14.5px}
  .web span{color:var(--leaf)}
  .footer-badges{flex:1;background:var(--leaf);display:flex;align-items:center;gap:18px;padding-left:12px}
  .badge-a{width:58px;height:58px;border-radius:8px;background:var(--leaf-deep);border:2px solid var(--white)}
  .badge-b{width:70px;height:70px;border-radius:50%;background:var(--panel-grey);border:4px solid var(--grey)}
  .badge-c{width:104px;height:42px;border-radius:6px;background:#1d4f8a}
  .badge-d{width:42px;height:72px;background:var(--leaf-deep);border:2px solid var(--white)}
  .license{font-family:"Oswald",sans-serif;font-weight:500;font-size:19px;color:var(--white);margin-left:-10px}
</style>
</head>
<body>
<div class="flyer">
  <header class="brand">
    <div class="brand-name"><span class="brand-dot"></span>canopy crest</div>
    <div class="brand-rule"></div>
    <div class="brand-tag">PROFESSIONAL TREE CARE</div>
  </header>

  <div class="photo photo-crew" role="img" aria-label="Tree crew in safety vests removing a tall pine in a backyard"></div>
  <section class="box about">
    <h2>ABOUT US</h2>
    <p>Canopy Crest Professional Tree Care has a GWF-Certified Arborist on staff and is fully licensed and insured for our customers’ protection. We maintain a clean, organized, and safe working environment and do the best we can to interfere as little as possible with your daily life.</p>
  </section>
  <div class="photo photo-trucks" role="img" aria-label="Bucket trucks parked beneath palm trees on a job site"></div>

  <section class="box areas">
    <h2>AREAS WE SERVICE</h2>
    <p>We service the Tampa Bay area including St. Petersburg, Clearwater, Belleair, Seminole, and surrounding areas.</p>
  </section>
  <div class="photo photo-loader" role="img" aria-label="Yellow compact tracked loader with crew members in the background"></div>

  <div class="specs-head"><h2>OUR SPECIALTIES</h2></div>
  <section class="specs" role="img" aria-label="Arborist in helmet and branded shirt, tinted green, behind the list of specialties">
    <ul>
      <li><svg width="44" height="44" viewBox="0 0 44 44"><circle cx="22" cy="22" r="20" fill="none" stroke="#fff" stroke-width="2"/><circle cx="22" cy="22" r="13" fill="#fff"/><circle cx="22" cy="22" r="4" fill="#3f9130"/></svg>Hurricane Preparedness</li>
      <li><svg width="44" height="44" viewBox="0 0 44 44"><circle cx="22" cy="22" r="20" fill="none" stroke="#fff" stroke-width="2"/><circle cx="22" cy="22" r="13" fill="#fff"/><path d="M16 27l12-10" stroke="#3f9130" stroke-width="3"/></svg>Tree Pruning</li>
      <li><svg width="44" height="44" viewBox="0 0 44 44"><circle cx="22" cy="22" r="20" fill="none" stroke="#fff" stroke-width="2"/><circle cx="22" cy="22" r="13" fill="#fff"/><path d="M16 22h12" stroke="#3f9130" stroke-width="3"/></svg>Trimming</li>
      <li><svg width="44" height="44" viewBox="0 0 44 44"><circle cx="22" cy="22" r="20" fill="none" stroke="#fff" stroke-width="2"/><circle cx="22" cy="22" r="13" fill="#fff"/><path d="M17 17l10 10M27 17l-10 10" stroke="#3f9130" stroke-width="3"/></svg>Removal</li>
      <li><svg width="44" height="44" viewBox="0 0 44 44"><circle cx="22" cy="22" r="20" fill="none" stroke="#fff" stroke-width="2"/><circle cx="22" cy="22" r="13" fill="#fff"/><path d="M22 15v14M17 29h10" stroke="#3f9130" stroke-width="3"/></svg>Support</li>
      <li><svg width="44" height="44" viewBox="0 0 44 44"><circle cx="22" cy="22" r="20" fill="none" stroke="#fff" stroke-width="2"/><circle cx="22" cy="22" r="13" fill="#fff"/><path d="M22 29v-9M22 22c-4 0-6-3-6-6 4 0 6 3 6 6zM22 22c4 0 6-3 6-6-4 0-6 3-6 6z" stroke="#3f9130" stroke-width="2" fill="#3f9130"/></svg>Planting</li>
      <li><svg width="44" height="44" viewBox="0 0 44 44"><circle cx="22" cy="22" r="20" fill="none" stroke="#fff" stroke-width="2"/><circle cx="22" cy="22" r="13" fill="#fff"/><path d="M22 15v7l5 3" stroke="#3f9130" stroke-width="2.5" fill="none"/></svg><span>Emergency Tree Service<br>And Much More</span></li>
    </ul>
  </section>

  <footer class="footer">
    <div class="footer-cta">
      <div class="cta-line">Call us to schedule a <strong>FREE</strong> estimate</div>
      <div class="contact">
        <span class="phone">1-866-413-BOUGH</span>
        <span class="web"><svg width="14" height="14" viewBox="0 0 14 14"><circle cx="7" cy="7" r="6" fill="none" stroke="#6fbe44" stroke-width="1.3"/><ellipse cx="7" cy="7" rx="2.5" ry="6" fill="none" stroke="#6fbe44" stroke-width="1"/><path d="M1 7h12" stroke="#6fbe44" stroke-width="1"/></svg>www.<span>canopycrestcare</span>.com</span>
      </div>
    </div>
    <div class="footer-badges">
      <div class="badge-a" role="img" aria-label="Review listing badge"></div>
      <div class="badge-b" role="img" aria-label="Screened and approved badge"></div>
      <div class="badge-c" role="img" aria-label="Business rating badge"></div>
      <div class="badge-d" role="img" aria-label="Certified arborist badge"></div>
      <span class="license">FL-4820K</span>
    </div>
  </footer>
</div>
</body>
</html>
```